diesel mechanic business card design

summit diesel is a new and upcoming business we are looking for some bad ass designs to help get us started we offer 24 hour road service, off road recovery, welding and custom fabrications we are diesel mechanics so our design should be bold and eye catching flames wrenches engine parts are cool we work in an industrial environment around heavy trucks and equipment this in not a quikko oil we fix it all nothing is to big or to small the colors red and black are always a plus but we are open to anything you guys can come up with ready set go

Target Market(s)

other small business primarily trucking and transportation companys

Industry/Entity Type

Business

Contact Information for Business Card

company name Sumitt diesel truck & trailer repair / address 14 rear north holbrin ave taylor PA 18503 / ownersAdam DeLuccie 570-555-0143 / Curtis Lavandel 570-555-0178 E mail brentmarvoski@mailvex.com fax 570-555-0192

Requirements
Nice to have
• industrial modern design
Should not have
• rainbows butterfly's unicorns or cupcakes

```html
<!DOCTYPE html>
<html lang="en">
<head>
<meta charset="utf-8">
<title>Kestrel Heavy Rig &amp; Hauler Service – Appointment Card</title>
<link rel="stylesheet" href="https://fonts.googleapis.com/css2?family=Russo+One&family=Josefin+Sans:wght@400;600&family=Philosopher:wght@700&display=swap">
<style>
  :root {
    --plank-dark: #141414;
    --plank-mid: #2b2b2b;
    --brand-red: #e3141b;
    --address-grey: #d6d8dc;
    --frame-orange: #ff5a00;
    --panel-olive: #7b7a4c;
    --panel-white: #ffffff;
    --panel-tan: #c9c3a4;
    --panel-pale: #e8ebd0;
    --ink: #1a1a1a;
  }
  * { margin: 0; padding: 0; box-sizing: border-box; }
  html, body { width: 1200px; height: 719px; overflow: hidden; background: #111; }
  .card { position: relative; width: 1200px; height: 719px; overflow: hidden; }
  .card__backdrop {
    position: absolute; inset: 0;
    background: linear-gradient(180deg, var(--plank-mid) 0%, var(--plank-dark) 45%, var(--plank-mid) 70%, var(--plank-dark) 100%);
  }
  .brand {
    position: absolute; right: 40px; top: 12px;
    width: 1140px; height: 170px;
    font-family: "Russo One", sans-serif;
    color: var(--brand-red);
    line-height: 1;
  }
  .brand__name {
    position: absolute; right: 0; top: 10px;
    font-size: 86px; white-space: nowrap;
  }
  .brand__tagline {
    position: absolute; right: 0; top: 108px;
    font-size: 54px; white-space: nowrap;
  }
  .address {
    position: absolute; left: 31px; top: 128px; width: 553px;
    text-align: center;
    font-family: "Josefin Sans", sans-serif;
    font-weight: 400; font-size: 44px; line-height: 60px;
    color: var(--address-grey);
    text-shadow: 3px 3px 4px #000;
    font-style: normal;
  }
  .appointment {
    position: absolute; left: 0; top: 282px;
    width: 1200px; height: 252px;
    border: 7px solid var(--frame-orange);
    background: linear-gradient(180deg,
      var(--panel-olive) 0%, #c8c8b0 30%,
      var(--panel-white) 52%, var(--panel-white) 60%,
      var(--panel-tan) 70%, var(--panel-pale) 76%, var(--panel-pale) 100%);
  }
  .appointment__title {
    position: absolute; top: 14px; width: 100%;
    text-align: center;
    font-family: "Philosopher", serif;
    font-weight: 700; font-size: 38px; letter-spacing: 1px;
    color: var(--ink);
  }
  .appointment__field {
    position: absolute; top: 150px; width: 367px;
    border-top: 2px solid var(--ink);
    padding-top: 6px;
    text-align: center;
    font-family: "Philosopher", serif;
    font-weight: 700; font-size: 27px;
    color: var(--ink);
  }
  .appointment__field--date { left: 172px; }
  .appointment__field--time { left: 647px; }
</style>
</head>
<body>
  <div class="card">
    <div class="card__backdrop" role="img" aria-label="Dark charcoal wood plank background texture"></div>

    <div class="brand">
      <span class="brand__name">Kestrel Heavy Rig</span>
      <span class="brand__tagline">&amp; Hauler Service</span>
    </div>

    <address class="address">
      212 Millrace Lane<br>
      Brackenford, OH 44890
    </address>

    <section class="appointment">
      <h2 class="appointment__title">My Appointment</h2>
      <div class="appointment__field appointment__field--date">Date of Appointment</div>
      <div class="appointment__field appointment__field--time">Time of Appointment</div>
    </section>
  </div>
</body>
</html>
```